Brochure for The Lantern Quay Lounge Private Venue

Brochure to sell the venue and food & beverage services for private parties
Venue name is The Lantern Quay Lounge

Target Market(s)

Age: 25 - 40 female

Industry/Entity Type

Events

Requirements
Must have
• Please also put the venue name, address, website and phone
• Lantern Quay Lounge
• 4871 Marigold Crest Blvd
• National City, CA 91950
• LanternQuay.Lounge
• (555) 318-7406
• TONS of photos. You can grab more photos if needed on the website
Nice to have
• Festive Vibe -

```html
<!DOCTYPE html>
<html lang="en">
<head>
<meta charset="utf-8">
<title>The Lantern Quay Lounge – Brochure</title>
<link href="https://fonts.googleapis.com/css2?family=Libre+Baskerville:wght@700&family=Open+Sans:wght@400;600;700&display=swap" rel="stylesheet">
<style>
  :root {
    --backdrop: #e4e4e6;
    --paper: #ffffff;
    --paper-shade: #f2f2f2;
    --orange: #f2a71b;
    --blue: #3a8fd0;
    --ink: #2b2b2b;
    --muted: #5b5b5b;
    --heading: #e5801e;
    --name-ink: #1f1f1f;
  }
  * { box-sizing: border-box; margin: 0; padding: 0; }
  html, body { width: 900px; height: 1200px; overflow: hidden; }
  body {
    background: var(--backdrop);
    font-family: "Open Sans", Arial, sans-serif;
    position: relative;
  }
  .spread {
    position: absolute;
    left: 30px; top: 303px;
    width: 840px; height: 594px;
    display: flex;
    box-shadow: 0 18px 40px rgba(0,0,0,.18);
  }
  .page {
    position: relative;
    width: 420px; height: 594px;
    background: var(--paper);
    overflow: hidden;
  }
  .page--back { background: linear-gradient(90deg, var(--paper) 0%, var(--paper-shade) 100%); }

  /* back page */
  .back-photo {
    position: absolute; left: 0; top: 28px; width: 420px; height: 372px;
    background:
      radial-gradient(ellipse 30% 18% at 62% 48%, #f4f4f2 0%, rgba(244,244,242,0) 100%),
      radial-gradient(ellipse 26% 16% at 82% 52%, #f1f1ef 0%, rgba(241,241,239,0) 100%),
      radial-gradient(ellipse 28% 12% at 55% 80%, #d98f8f 0%, rgba(217,143,143,0) 100%),
      linear-gradient(170deg, #e6e4e0 0%, #cfc7c0 28%, #9c7a62 52%, #6e3f24 72%, #552f1b 100%);
  }
  .back-intro {
    position: absolute; left: 26px; top: 410px; width: 372px;
    font-size: 10.5px; line-height: 1.45; font-weight: 600; color: var(--ink);
  }
  .back-title {
    position: absolute; left: 26px; top: 446px;
    font-family: "Libre Baskerville", Georgia, serif;
    font-size: 17px; color: var(--heading);
  }
  .back-tagline {
    position: absolute; left: 26px; top: 471px;
    font-size: 11px; text-transform: uppercase; color: var(--muted); letter-spacing: .2px;
  }
  .contact-bar {
    position: absolute; left: 0; top: 498px; width: 420px; height: 44px;
    background: var(--blue);
    color: #fff; font-size: 11px;
  }
  .contact-bar .web { position: absolute; left: 24px; top: 6px; display: flex; align-items: center; gap: 6px; }
  .contact-bar .phone { position: absolute; right: 44px; top: 24px; display: flex; align-items: center; gap: 6px; }

  /* front page */
  .venue-mark {
    position: absolute; left: 0; top: 26px; width: 420px;
    display: flex; justify-content: center; align-items: center; gap: 8px;
    font-weight: 700; font-size: 20px; color: var(--name-ink);
  }
  .venue-mark .dot { width: 12px; height: 12px; background: var(--orange); }
  .front-photo {
    position: absolute; left: 0; top: 78px; width: 420px; height: 412px;
    background:
      radial-gradient(ellipse 10% 7% at 26% 38%, #ffffff 0%, rgba(255,255,255,0) 100%),
      radial-gradient(ellipse 9% 6% at 44% 46%, #ffffff 0%, rgba(255,255,255,0) 100%),
      radial-gradient(ellipse 22% 12% at 78% 58%, #f6f1ee 0%, rgba(246,241,238,0) 100%),
      linear-gradient(180deg, #222 0%, #3a3a3a 10%, #d9d9d9 22%, #ebe8e6 45%, #b08a6c 62%, #7a5234 74%, #5d5853 100%);
  }
  .event-banner {
    position: absolute; left: 14px; top: 432px; width: 400px; height: 76px;
    background: var(--orange);
    clip-path: polygon(0 8%, 100% 0, 96% 100%, 0 100%);
    padding: 16px 0 0 16px;
    font-family: "Libre Baskerville", Georgia, serif;
    color: #fff; font-size: 14.5px; line-height: 1.32; text-transform: uppercase;
  }
  .address-bar {
    position: absolute; left: 0; top: 526px; width: 420px; height: 44px;
    background: var(--blue);
    color: #fff; font-size: 12px;
    display: flex; align-items: center; gap: 8px; padding-left: 22px;
  }
</style>
</head>
<body>
  <div class="spread">
    <section class="page page--back">
      <div class="back-photo" role="img" aria-label="Close-up of a set wooden table with pink napkins, gold chargers, white paper lanterns and flowers"></div>
      <p class="back-intro">Lantern Quay Lounge is a private event venue and club located 5 minutes south of downtown San Diego in National City.</p>
      <h2 class="back-title">The Lantern Quay Lounge</h2>
      <p class="back-tagline">Elegant wedding &amp; event venue, just south of downtown SD</p>
      <div class="contact-bar">
        <span class="web">
          <svg width="10" height="10" viewBox="0 0 10 10"><circle cx="5" cy="5" r="4" fill="none" stroke="#fff" stroke-width="1"/><path d="M1 5h8M5 1v8" stroke="#fff" stroke-width=".8"/></svg>
          www.lanternquay.lounge
        </span>
        <span class="phone">
          <svg width="10" height="10" viewBox="0 0 10 10"><path d="M2 1l2 2-1 1.5c.8 1.4 1.6 2.2 3 3L7.5 6 9.5 8 8 9.5C4.5 9 1 5.5.5 2z" fill="#fff"/></svg>
          (555) 318-7406
        </span>
      </div>
    </section>

    <section class="page page--front">
      <div class="venue-mark"><span class="dot"></span>Lantern Quay Lounge</div>
      <div class="front-photo" role="img" aria-label="Event hall set with long wooden tables, cross-back chairs, white lanterns and string lights"></div>
      <h1 class="event-banner">Birthday Party, Baby Shower<br>Celebration of Life, or Quincenira</h1>
      <div class="address-bar">
        <svg width="12" height="14" viewBox="0 0 12 14"><path d="M6 0a5 5 0 0 1 5 5c0 3.5-5 9-5 9S1 8.5 1 5a5 5 0 0 1 5-5z" fill="#fff"/><circle cx="6" cy="5" r="2" fill="#3a8fd0"/></svg>
        4871 Marigold Crest Blvd National City, CA 91950
      </div>
    </section>
  </div>
</body>
</html>
```